Varlow Landscaping

Create a website for a new landscaping company. I have a logo already and description of services offered. I have a website that I would like all inquiries and appointments to get forwarded to. I need just need it well organized so that a husband and wife team can manage it easily. This is a company that will continue to grow over time and will need to add more services under new tabs over time. If you need the email where appointments and inquiries should go please send me a message.
Services offered are: Weekly/bi weekly mowing, weed eating and edging, Plant installation pinestraw & mulch installation, weed & feed, leaf removal and yard clean up.

```html
<!DOCTYPE html>
<html lang="en">
<head>
<meta charset="utf-8">
<title>Varlow Landscaping</title>
<link href="https://fonts.googleapis.com/css2?family=Outfit:wght@300;400;500;600;700;800&display=swap" rel="stylesheet">
<style>
:root{
  --green:#3f9b14;
  --green-light:#7cc22a;
  --yellow:#efc410;
  --dark:#2f352c;
  --text:#555a52;
  --cream:#f1f0e8;
  --white:#ffffff;
}
*{box-sizing:border-box;margin:0;padding:0}
html,body{width:1200px;height:4409px;overflow:hidden}
body{position:relative;font-family:'Outfit',sans-serif;color:var(--dark);background:var(--white)}
.abs{position:absolute}
.brand{font-family:'Outfit',sans-serif;font-weight:700;color:var(--green);text-transform:uppercase;line-height:1.05;text-align:center;display:flex;align-items:center;gap:8px}
.brand .dot{width:18px;height:18px;border-radius:50%;background:var(--yellow);flex:none}
/* header */
.topbar{left:575px;top:0;width:625px;height:31px;background:var(--green);border-bottom-left-radius:14px;display:flex;align-items:center;justify-content:space-around;color:#fff;font-size:10px}
.topbar span{display:flex;align-items:center;gap:6px}
.nav{left:482px;top:68px;display:flex;gap:24px;font-size:10px;font-weight:500;text-transform:uppercase;color:#444}
.nav .active{color:var(--green);font-weight:700}
.btn{display:flex;align-items:center;justify-content:space-between;border-radius:30px;color:#fff;font-weight:600;text-transform:uppercase;font-size:9.5px;padding:0 5px 0 24px}
.btn .arrow{width:28px;height:28px;border-radius:50%;background:#fff;display:flex;align-items:center;justify-content:center}
.btn-yellow{background:var(--yellow)}
.btn-green{background:var(--green-light)}
/* hero */
.hero{left:0;top:116px;width:1200px;height:629px;background:linear-gradient(100deg,#2d3a18 0%,#4f6a22 35%,#7f9c35 60%,#a9a86a 80%,#6f7c3f 100%)}
.hero-title{left:123px;top:272px;font-size:51px;font-weight:800;line-height:1.05;color:#fff;text-transform:uppercase}
.hero-sub{left:123px;top:446px;font-size:19px;font-weight:700;color:#fff;text-transform:uppercase}
.hero-text{left:123px;top:486px;font-size:12px;color:#fff;text-transform:uppercase;line-height:1.45}
.dots{left:125px;top:681px;display:flex;gap:8px}
.dots i{width:11px;height:11px;border-radius:50%;background:#fff;opacity:.5}
.dots i:first-child,.dots i:last-child{opacity:1}
/* sections */
.section-title{width:1200px;left:0;text-align:center;font-weight:700;text-transform:uppercase;letter-spacing:-.5px}
.service-band{left:0;top:745px;width:1200px;height:330px;background:var(--yellow)}
.card{width:204px;height:243px;top:906px;border-radius:12px}
.card-label{width:204px;top:1159px;text-align:center;font-size:11px;font-weight:600;text-transform:uppercase;line-height:1.45;color:#333}
.round{width:46px;height:46px;border-radius:50%;display:flex;align-items:center;justify-content:center}
.photo{border-radius:10px}
.why{left:0;top:1763px;width:1200px;height:569px;background:var(--cream)}
.feat{width:260px}
.feat h4{font-size:11px;font-weight:700;text-transform:uppercase;color:#222;margin-bottom:3px}
.feat p{font-size:9.5px;line-height:1.35;color:var(--text)}
.feat-icon{width:78px;height:78px;border-radius:50%;display:flex;align-items:center;justify-content:center}
.contact{left:0;top:3330px;width:1200px;height:626px;background:var(--green-light)}
.label{font-size:8px;font-weight:700;color:#fff;text-transform:uppercase}
.field{background:#fff;border-radius:24px;font-size:10px;color:#555;padding:0 22px;display:flex;align-items:center}
.footer{left:0;top:3956px;width:1200px;height:453px;background:var(--cream)}
.foot-nav{left:0;width:1200px;top:4192px;display:flex;justify-content:center;gap:30px;font-size:9.5px;text-transform:uppercase;color:#444}
.foot-nav span::before{content:"•";color:var(--yellow);margin-right:12px}
.foot-nav span:first-child::before{content:none}
.foot-contact{display:flex;align-items:center;gap:14px;font-size:10px;color:#333}
.foot-contact .round{width:38px;height:38px}
.social{width:24px;height:24px;border-radius:50%;border:1.5px solid #555}
</style>
</head>
<body>

<!-- Header -->
<div class="abs brand" style="left:122px;top:30px;font-size:21px"><span class="dot"></span><span>Varlow<br><span style="font-size:12px">Landscaping</span></span></div>
<div class="abs topbar">
  <span><svg width="10" height="10" viewBox="0 0 24 24" fill="#fff"><path d="M6.6 10.8a15 15 0 006.6 6.6l2.2-2.2a1 1 0 011-.25 11.4 11.4 0 003.6.6 1 1 0 011 1V20a1 1 0 01-1 1A17 17 0 013 4a1 1 0 011-1h3.5a1 1 0 011 1c0 1.25.2 2.45.6 3.6a1 1 0 01-.25 1z"/></svg>(123) 456-7890</span>
  <span><svg width="10" height="10" viewBox="0 0 24 24" fill="#fff"><path d="M2 5h20v14H2z"/><path d="M2 5l10 8 10-8" stroke="#3f9b14" stroke-width="2" fill="none"/></svg>info@example.com</span>
  <span><svg width="9" height="11" viewBox="0 0 24 30" fill="#fff"><path d="M12 0a10 10 0 00-10 10c0 8 10 20 10 20s10-12 10-20A10 10 0 0012 0zm0 14a4 4 0 110-8 4 4 0 010 8z"/></svg>Some address goes here</span>
</div>
<nav class="abs nav"><span class="active">Home</span><span>Services</span><span>About Us</span><span>Gallery</span><span>Testimonials</span><span>Contact Us</span></nav>
<div class="abs btn btn-yellow" style="left:902px;top:55px;width:170px;height:39px"><span>Book Appointment</span><span class="arrow"><svg width="10" height="10" viewBox="0 0 10 10"><path d="M3 1l4 4-4 4" stroke="#333" stroke-width="1.6" fill="none"/></svg></span></div>

<!-- Hero -->
<div class="abs hero" role="img" aria-label="Photo of a green lawn with a curved stone path leading to a house at sunset"></div>
<h1 class="abs hero-title">Transform<br>your outdoors<br>with expert</h1>
<div class="abs hero-sub">Landscaping Services</div>
<p class="abs hero-text">From lawn care to complete yard transformations<br>we've got you covered!</p>
<div class="abs btn btn-yellow" style="left:123px;top:543px;width:165px;height:37px"><span>Get a free quote</span><span class="arrow"><svg width="10" height="10" viewBox="0 0 10 10"><path d="M3 1l4 4-4 4" stroke="#333" stroke-width="1.6" fill="none"/></svg></span></div>
<div class="abs dots"><i></i><i></i><i></i></div>

<!-- Services -->
<div class="abs service-band"></div>
<h2 class="abs section-title" style="top:815px;font-size:31px;color:#fff">Our Service</h2>
<p class="abs section-title" style="top:862px;font-size:10px;font-weight:400;color:#fff;text-transform:none;letter-spacing:0">Professional Landscaping Services Tailored to Your Needs</p>
<div class="abs card" style="left:163px;background:linear-gradient(160deg,#4f7a2c,#7bb04a)" role="img" aria-label="Photo of a worker on a riding mower"></div>
<div class="abs card" style="left:386px;background:linear-gradient(160deg,#c9cdd2,#6f8f45)" role="img" aria-label="Photo of a worker with a string trimmer"></div>
<div class="abs card" style="left:610px;background:linear-gradient(160deg,#e7ecef,#5f8d36)" role="img" aria-label="Photo of a gardener planting a shrub"></div>
<div class="abs card" style="left:832px;background:linear-gradient(160deg,#5f8d36,#6d4b30)" role="img" aria-label="Photo of a landscaper inspecting a mulch bed"></div>
<div class="abs card-label" style="left:163px">Weekly / Bi Weekly<br>Mowing</div>
<div class="abs card-label" style="left:386px">Weed Eating<br>&amp; Edging</div>
<div class="abs card-label" style="left:610px">Plant<br>Installation</div>
<div class="abs card-label" style="left:832px">Pinestraw &amp; Mulch<br>Installation</div>
<div class="abs round" style="left:550px;top:1215px;background:var(--green-light)"><svg width="10" height="10" viewBox="0 0 10 10"><path d="M7 1L3 5l4 4" stroke="#fff" stroke-width="1.6" fill="none"/></svg></div>
<div class="abs round" style="left:604px;top:1215px;background:var(--yellow)"><svg width="10" height="10" viewBox="0 0 10 10"><path d="M3 1l4 4-4 4" stroke="#fff" stroke-width="1.6" fill="none"/></svg></div>

<!-- About -->
<div class="abs photo" style="left:168px;top:1351px;width:215px;height:150px;background:linear-gradient(180deg,#3a5a22,#6fbf2e)" role="img" aria-label="Photo of a freshly mowed lawn"></div>
<div class="abs photo" style="left:168px;top:1513px;width:215px;height:151px;background:linear-gradient(180deg,#8aa56a,#4f7e2e)" role="img" aria-label="Photo of a man mowing a garden lawn"></div>
<div class="abs photo" style="left:397px;top:1351px;width:219px;height:313px;background:linear-gradient(180deg,#3f4a3a,#6e7d44 55%,#8a6a48)" role="img" aria-label="Photo of a worker using a lawn aerator"></div>
<h2 class="abs" style="left:666px;top:1372px;font-size:31px;font-weight:700;line-height:1.05;text-transform:uppercase">Welcome Varlow<br>Meet the experts<br>behind</h2>
<div class="abs" style="left:666px;top:1486px;width:68px;height:3px;background:linear-gradient(90deg,var(--green-light) 50%,var(--yellow) 50%)"></div>
<p class="abs" style="left:666px;top:1505px;width:370px;font-size:10px;line-height:1.55;color:var(--text)">We are a husband and wife team passionate about creating beautiful outdoor spaces for homeowners. With over X years of experience, we pride ourselves on providing personalized services to meet your landscaping needs. Our mission is to deliver professional and affordable solutions to keep your yard looking its best all year round.</p>
<div class="abs btn btn-green" style="left:666px;top:1604px;width:134px;height:38px"><span>Read More</span><span class="arrow"><svg width="10" height="10" viewBox="0 0 10 10"><path d="M3 1l4 4-4 4" stroke="#333" stroke-width="1.6" fill="none"/></svg></span></div>

<!-- Why choose -->
<div class="abs why"></div>
<h2 class="abs section-title" style="top:1822px;font-size:30px">Why Choose Varlow</h2>
<div class="abs" style="left:437px;top:1900px;width:326px;height:326px;border-radius:50%;border:8px solid var(--green);background:#fff;box-shadow:0 0 0 4px #ddd inset"></div>
<div class="abs brand" style="left:437px;top:2030px;width:326px;justify-content:center;font-size:30px;flex-direction:column;gap:6px"><span class="dot"></span><span>Varlow<br><span style="font-size:17px">Landscaping</span></span></div>

<div class="abs feat" style="left:53px;top:1920px;text-align:right"><h4>Licensed and Insured</h4><p>We are a husband and wife team<br>passionate about creating</p></div>
<div class="abs feat-icon" style="left:329px;top:1902px;background:var(--green-light)"><svg width="34" height="34" viewBox="0 0 24 24" fill="none" stroke="#fff" stroke-width="1.6"><rect x="4" y="3" width="16" height="18" rx="2"/><path d="M8 12l3 3 5-6"/></svg></div>
<div class="abs feat" style="left:53px;top:2043px;text-align:right"><h4>24 Hour Emergency</h4><p>We are a husband and wife team<br>passionate about creating</p></div>
<div class="abs feat-icon" style="left:329px;top:2027px;background:var(--yellow)"><svg width="36" height="36" viewBox="0 0 24 24" fill="none" stroke="#fff" stroke-width="1.6"><circle cx="12" cy="12" r="9"/><text x="12" y="15" font-size="8" text-anchor="middle" fill="#fff" stroke="none" font-family="Outfit,sans-serif" font-weight="700">24</text></svg></div>
<div class="abs feat" style="left:53px;top:2172px;text-align:right"><h4>Locally Owned</h4><p>We are a husband and wife team<br>passionate about creating</p></div>
<div class="abs feat-icon" style="left:329px;top:2151px;background:var(--green-light)"><svg width="28" height="34" viewBox="0 0 24 30" fill="none" stroke="#fff" stroke-width="2"><path d="M12 2a9 9 0 00-9 9c0 7 9 17 9 17s9-10 9-17a9 9 0 00-9-9z"/><circle cx="12" cy="11" r="3.5"/></svg></div>

<div class="abs feat-icon" style="left:793px;top:1902px;background:var(--green-light)"><svg width="34" height="34" viewBox="0 0 24 24" fill="#fff"><path d="M7 3l5 8H9l4 6H1l4-6H2z"/><path d="M17 5l4 7h-2l3 5h-10l3-5h-2z"/></svg></div>
<div class="abs feat" style="left:887px;top:1920px"><h4>Professionl Work</h4><p>We are a husband and wife team<br>passionate about creating</p></div>
<div class="abs feat-icon" style="left:793px;top:2027px;background:var(--yellow)"><svg width="34" height="34" viewBox="0 0 24 24" fill="none" stroke="#fff" stroke-width="1.8"><path d="M12 2l8 3v6c0 5-3.5 9-8 11-4.5-2-8-6-8-11V5z"/><path d="M8 12l3 3 5-6"/></svg></div>
<div class="abs feat" style="left:887px;top:2043px"><h4>Safety is our top priority</h4><p>We are a husband and wife team<br>passionate about creating</p></div>
<div class="abs feat-icon" style="left:793px;top:2151px;background:var(--green-light)"><svg width="32" height="34" viewBox="0 0 24 24" fill="none" stroke="#fff" stroke-width="1.6"><rect x="5" y="3" width="14" height="18" rx="2"/><path d="M8 8h8M8 12h8M8 16h5"/></svg></div>
<div class="abs feat" style="left:887px;top:2172px"><h4>Free Estimate</h4><p>We are a husband and wife team<br>passionate about creating</p></div>

<!-- Testimonials -->
<h2 class="abs section-title" style="top:2414px;font-size:30px">What our clients are saying</h2>
<div class="abs section-title" style="top:2452px;font-size:120px;color:var(--yellow);line-height:1;font-weight:800">&ldquo;</div>
<p class="abs section-title" style="top:2546px;font-size:14px;font-weight:400;text-transform:none;line-height:1.55;color:var(--text);letter-spacing:0">"Excellent service! Our yard looks amazing thanks to [Company Name]. The team<br>was professional, punctual, and extremely thorough. They really transformed our<br>space into something we love spending time in."</p>
<div class="abs section-title" style="top:2622px;font-size:13px;letter-spacing:0">Mara &amp; Tom L.</div>
<div class="abs section-title" style="top:2645px;font-size:13px;color:var(--yellow);letter-spacing:1px">★★★★★</div>
<div class="abs" style="left:1060px;top:2524px;display:flex;flex-direction:column;gap:9px">
  <i style="width:11px;height:11px;border-radius:50%;background:#a9d67a;display:block"></i>
  <i style="width:11px;height:11px;border-radius:50%;background:var(--green);display:block"></i>
  <i style="width:11px;height:11px;border-radius:50%;background:#a9d67a;display:block"></i>
</div>

<!-- Projects -->
<h2 class="abs section-title" style="top:2744px;font-size:30px">Our Recent Projects</h2>
<div class="abs photo" style="left:183px;top:2813px;width:269px;height:167px;background:linear-gradient(160deg,#9aa09a,#c05a9c 55%,#5f9c35)" role="img" aria-label="Photo of a colourful flower bed in front of a house"></div>
<div class="abs photo" style="left:183px;top:2992px;width:269px;height:166px;background:linear-gradient(170deg,#4d7a3a,#8aa34b 55%,#7a6648)" role="img" aria-label="Photo of a worker laying sod rolls"></div>
<div class="abs photo" style="left:466px;top:2813px;width:268px;height:345px;background:linear-gradient(170deg,#4f8a2c,#7fae3c 60%,#3f6d22)" role="img" aria-label="Photo of a gardener with a wheelbarrow"></div>
<div class="abs" style="left:582px;top:2949px;width:34px;height:34px;border-radius:50%;background:#fff;display:flex;align-items:center;justify-content:center"><svg width="12" height="12" viewBox="0 0 24 24" fill="none" stroke="#333" stroke-width="2.5"><circle cx="10" cy="10" r="6"/><path d="M15 15l6 6"/></svg></div>
<div class="abs" style="left:582px;top:2993px;width:34px;height:34px;border-radius:50%;background:#fff;display:flex;align-items:center;justify-content:center"><svg width="12" height="12" viewBox="0 0 24 24" fill="none" stroke="#333" stroke-width="2.5"><path d="M10 14a4 4 0 005.7 0l3-3a4 4 0 00-5.7-5.7l-1 1M14 10a4 4 0 00-5.7 0l-3 3a4 4 0 005.7 5.7l1-1"/></svg></div>
<div class="abs photo" style="left:748px;top:2813px;width:267px;height:167px;background:linear-gradient(170deg,#3d5c2a,#6ea640)" role="img" aria-label="Photo of a worker pushing a lawn mower"></div>
<div class="abs photo" style="left:748px;top:2992px;width:267px;height:166px;background:linear-gradient(170deg,#3f6a28,#6b4a30 60%,#7eb94a)" role="img" aria-label="Photo of a fresh mulch bed with shrubs"></div>
<div class="abs round" style="left:550px;top:3190px;background:var(--green-light)"><svg width="10" height="10" viewBox="0 0 10 10"><path d="M7 1L3 5l4 4" stroke="#fff" stroke-width="1.6" fill="none"/></svg></div>
<div class="abs round" style="left:604px;top:3190px;background:var(--yellow)"><svg width="10" height="10" viewBox="0 0 10 10"><path d="M3 1l4 4-4 4" stroke="#fff" stroke-width="1.6" fill="none"/></svg></div>

<!-- Contact -->
<div class="abs contact"></div>
<h2 class="abs section-title" style="top:3391px;font-size:30px;color:#fff">Get in touch with us</h2>
<div class="abs label" style="left:228px;top:3451px">Name*</div>
<div class="abs field" style="left:228px;top:3468px;width:366px;height:45px">Enter your name</div>
<div class="abs label" style="left:604px;top:3451px">Phone*</div>
<div class="abs field" style="left:604px;top:3468px;width:367px;height:45px">Enter your phone number</div>
<div class="abs label" style="left:228px;top:3531px">Email*</div>
<div class="abs field" style="left:228px;top:3548px;width:366px;height:45px">Enter your email</div>
<div class="abs label" style="left:604px;top:3531px">Address*</div>
<div class="abs field" style="left:604px;top:3548px;width:367px;height:45px">Enter your email address</div>
<div class="abs label" style="left:228px;top:3611px">Message*</div>
<div class="abs" style="left:228px;top:3628px;width:743px;height:222px;background:#fff;border-radius:22px"></div>
<div class="abs btn btn-yellow" style="left:534px;top:3876px;width:132px;height:39px;box-shadow:0 0 0 2px #fff inset"><span>Submit Now</span><span class="arrow"><svg width="10" height="10" viewBox="0 0 10 10"><path d="M3 1l4 4-4 4" stroke="#333" stroke-width="1.6" fill="none"/></svg></span></div>

<!-- Footer -->
<div class="abs footer"></div>
<div class="abs brand" style="left:0;top:4030px;width:1200px;justify-content:center;font-size:26px;flex-direction:column;gap:6px"><span class="dot"></span><span>Varlow<br><span style="font-size:15px">Landscaping</span></span></div>
<div class="abs" style="left:218px;top:4177px;width:777px;height:1px;background:#cfcfc4"></div>
<div class="abs foot-nav"><span style="color:var(--green-light)">Home</span><span>Services</span><span>About Us</span><span>Gallery</span><span>Testimonials</span><span>Contact Us</span></div>
<div class="abs foot-contact" style="left:217px;top:4245px"><span class="round" style="background:var(--green-light)"><svg width="15" height="15" viewBox="0 0 24 24" fill="#fff"><path d="M6.6 10.8a15 15 0 006.6 6.6l2.2-2.2a1 1 0 011-.25 11.4 11.4 0 003.6.6 1 1 0 011 1V20a1 1 0 01-1 1A17 17 0 013 4a1 1 0 011-1h3.5a1 1 0 011 1c0 1.25.2 2.45.6 3.6a1 1 0 01-.25 1z"/></svg></span>(123) 456-7890</div>
<div class="abs foot-contact" style="left:361px;top:4245px"><span class="round" style="background:var(--yellow)"><svg width="15" height="15" viewBox="0 0 24 24" fill="#fff"><path d="M2 5h20v14H2z"/><path d="M2 5l10 8 10-8" stroke="#efc410" stroke-width="2" fill="none"/></svg></span>info@example.com</div>
<div class="abs foot-contact" style="left:528px;top:4245px"><span class="round" style="background:var(--green-light)"><svg width="13" height="16" viewBox="0 0 24 30" fill="#fff"><path d="M12 0a10 10 0 00-10 10c0 8 10 20 10 20s10-12 10-20A10 10 0 0012 0zm0 14a4 4 0 110-8 4 4 0 010 8z"/></svg></span>Some address goes here</div>
<div class="abs" style="left:873px;top:4252px;display:flex;gap:7px"><i class="social"></i><i class="social"></i><i class="social"></i><i class="social"></i></div>
<div class="abs section-title" style="top:4377px;font-size:9.5px;font-weight:400;letter-spacing:0;color:#444">© 2026 Varlow. All rights reserved.</div>
<div class="abs round" style="left:1116px;top:4336px;width:42px;height:42px;background:var(--yellow)"><svg width="12" height="12" viewBox="0 0 10 10"><path d="M1 7l4-4 4 4" stroke="#fff" stroke-width="1.6" fill="none"/></svg></div>

</body>
</html>
```